Social Media Graphics - Harbor Climb REVISED

Create 6-7 individual social media graphics (square size) to encourage folks to join our online course called:

The Lantern Ledger Plan
How to Launch a Multi-Million Business From Scratch
Sign Up Today!

IMPORTANT: Make the largest and most prominent text on the graphic be: How to Launch a Multi-Million Business From Scratch

For the color scheme of the graphics, let's try a blue color palette; make sure the graphics appeal to both men and women

Make sure each graphic contains 1 of the 3 pics attached (crop pic as needed); and make sure one of the graphics is all TEXT only.

Target Market(s)

men and women looking to start a business

Industry/Entity Type

Entrepreneurship

Colors
0054AA
0677BA
7BADD7
CADEEF
E8F1F8

Requirements
Must have
• All the text and use the 3 pics provided; one graphic can be all text; Simple, modern design that's easy to read

```html
<!DOCTYPE html>
<html lang="en">
<head>
<meta charset="UTF-8">
<title>Harbor Climb – The Lantern Ledger Plan</title>
<link href="https://fonts.googleapis.com/css2?family=Anton&family=Oswald:wght@700&display=swap" rel="stylesheet">
<style>
  :root {
    --navy: #0b4585;
    --blue: #0054AA;
    --sky: #7BADD7;
    --mist: #CADEEF;
    --ice: #E8F1F8;
    --white: #ffffff;
  }
  html, body {
    margin: 0;
    padding: 0;
    overflow: hidden;
    background: var(--ice);
  }
  .graphic {
    position: relative;
    width: 1200px;
    height: 1200px;
    overflow: hidden;
    background: radial-gradient(circle at 45% 55%, #dbeefb 0%, #b9dcf3 55%, #9cc9ea 100%);
    font-family: "Anton", "Oswald", sans-serif;
  }
  .decor {
    position: absolute;
    inset: 0;
  }
  .hosts-photo {
    position: absolute;
    left: 150px;
    top: 70px;
    width: 900px;
    height: 600px;
  }
  .headline {
    position: absolute;
    left: 0;
    right: 0;
    text-align: center;
    margin: 0;
    text-transform: uppercase;
    color: var(--navy);
    -webkit-text-stroke: 6px var(--white);
    paint-order: stroke fill;
    letter-spacing: 1px;
    line-height: 1;
  }
  .headline-lead {
    top: 578px;
    font-size: 84px;
  }
  .headline-feature {
    top: 655px;
    font-size: 178px;
    color: #cfe6f7;
    -webkit-text-stroke: 5px var(--navy);
    transform: skewX(-14deg);
    letter-spacing: 2px;
  }
  .headline-tail {
    top: 803px;
    font-size: 84px;
  }
  .program-band {
    position: absolute;
    left: 135px;
    top: 897px;
    width: 960px;
    height: 235px;
    background: var(--navy);
    text-align: center;
    color: var(--white);
    text-transform: uppercase;
  }
  .program-band .line-one {
    display: block;
    font-size: 104px;
    line-height: 1;
    margin-top: 4px;
  }
  .program-band .line-two {
    display: block;
    font-size: 118px;
    line-height: 1;
    margin-top: 4px;
  }
  .cta {
    position: absolute;
    left: 0;
    right: 0;
    top: 1146px;
    text-align: center;
    font-family: "Oswald", sans-serif;
    font-weight: 700;
    font-size: 36px;
    color: var(--navy);
    text-transform: uppercase;
    letter-spacing: 0.5px;
    margin: 0;
  }
</style>
</head>
<body>
  <main class="graphic">
    <svg class="decor" width="1200" height="1200" viewBox="0 0 1200 1200" aria-hidden="true">
      <path fill-rule="evenodd" fill="var(--navy)"
        d="M800 -290 a380 380 0 1 0 0.1 0 Z M800 -140 a230 230 0 1 1 -0.1 0 Z"/>
      <path fill-rule="evenodd" fill="var(--navy)"
        d="M-20 810 a230 230 0 1 0 0.1 0 Z M-20 935 a105 105 0 1 1 -0.1 0 Z"/>
    </svg>

    <svg class="hosts-photo" role="img" aria-label="Photo of the two course hosts, a man in a black turtleneck and a woman in a denim blazer, smiling side by side" viewBox="0 0 900 600">
      <defs>
        <linearGradient id="photoTone" x1="0" y1="0" x2="1" y2="0">
          <stop offset="0" stop-color="#2a2a2e"/>
          <stop offset="0.5" stop-color="#4a3a34"/>
          <stop offset="1" stop-color="#1f4f86"/>
        </linearGradient>
        <linearGradient id="photoFade" x1="0" y1="0" x2="0" y2="1">
          <stop offset="0" stop-color="#fff"/>
          <stop offset="0.7" stop-color="#fff"/>
          <stop offset="1" stop-color="#fff" stop-opacity="0"/>
        </linearGradient>
        <mask id="photoMask">
          <rect width="900" height="600" fill="url(#photoFade)"/>
        </mask>
      </defs>
      <rect width="900" height="600" rx="40" fill="url(#photoTone)" mask="url(#photoMask)" opacity="0.85"/>
    </svg>

    <h1 class="headline headline-lead">How to Launch a</h1>
    <p class="headline headline-feature">Multi-Million</p>
    <p class="headline headline-tail">Business From Scratch</p>

    <div class="program-band">
      <span class="line-one">It’s The Lantern</span>
      <span class="line-two">Ledger Plan</span>
    </div>

    <p class="cta">Join the Beacon Community Today.</p>
  </main>
</body>
</html>
```